Electrical panel service sticker w Bucket truck & Logo

We have a rather plain sticker we put on lighting panels to remind customers who to call for service. We want to redesign them with brushed aluminum background. We want a remake of the sticker with the outline of a bucket truck. You'll need to find or draw the outling of a bucket truck maybe with the boom up slightly as we will get these stickers die cut.

We want LOGO with Ph.# and Email.
Electrical * Lighting * Sign Service

Target Market(s)

Commercial property managers

Industry/Entity Type

Property Management

Requirements
Must have
• Bucket Truck Outline

```html
<!DOCTYPE html>
<html lang="en">
<head>
<meta charset="utf-8">
<title>Panel Service Sticker</title>
<link href="https://fonts.googleapis.com/css2?family=Barlow+Condensed:wght@500;600;700&display=swap" rel="stylesheet">
<style>
  :root {
    --page-bg: #eeeeee;
    --metal-light: #d9dadb;
    --metal-mid: #b9babc;
    --metal-dark: #9c9d9f;
    --ink: #111111;
    --illustration-tone: #a4a5a7;
  }
  html, body {
    margin: 0;
    padding: 0;
    width: 1200px;
    height: 1200px;
    overflow: hidden;
    background: var(--page-bg);
  }
  .sticker {
    position: absolute;
    left: 78px;
    top: 288px;
    width: 1044px;
    height: 624px;
    background:
      repeating-linear-gradient(180deg, rgba(255,255,255,0.06) 0 1px, rgba(0,0,0,0.04) 1px 3px),
      linear-gradient(100deg, var(--metal-dark) 0%, var(--metal-light) 45%, var(--metal-mid) 70%, var(--metal-light) 100%);
    font-family: "Barlow Condensed", "Arial Narrow", sans-serif;
    color: var(--ink);
  }
  .services {
    position: absolute;
    left: 40px;
    top: 182px;
    margin: 0;
    padding: 0;
    list-style: none;
  }
  .services li {
    display: flex;
    align-items: center;
    height: 87px;
    font-size: 74px;
    font-weight: 600;
    letter-spacing: 1px;
    line-height: 1;
  }
  .services svg {
    width: 26px;
    height: 24px;
    margin-right: 14px;
  }
  .divider {
    position: absolute;
    left: 450px;
    top: 40px;
    width: 40px;
    height: 544px;
  }
  .truck-art {
    position: absolute;
    left: 562px;
    top: 62px;
    width: 385px;
    height: 253px;
    background: var(--illustration-tone);
    border-radius: 6px;
  }
  .contact {
    position: absolute;
    left: 510px;
    top: 332px;
    width: 500px;
    text-align: center;
  }
  .contact-lead {
    font-size: 70px;
    font-weight: 600;
    letter-spacing: 1px;
    line-height: 1;
    margin: 0;
  }
  .contact-phone {
    font-size: 98px;
    font-weight: 700;
    line-height: 1;
    margin: 14px 0 0;
  }
  .contact-email {
    font-size: 37px;
    font-weight: 500;
    line-height: 1;
    margin: 16px 0 0;
  }
</style>
</head>
<body>
  <main class="sticker">
    <ul class="services">
      <li><svg viewBox="0 0 26 24"><path d="M2 2 L24 12 L2 22 L8 12 Z" fill="currentColor"/></svg>ELECTRICAL</li>
      <li><svg viewBox="0 0 26 24"><path d="M2 2 L24 12 L2 22 L8 12 Z" fill="currentColor"/></svg>LIGHTING</li>
      <li><svg viewBox="0 0 26 24"><path d="M2 2 L24 12 L2 22 L8 12 Z" fill="currentColor"/></svg>SIGN SERVICE</li>
    </ul>

    <svg class="divider" viewBox="0 0 40 544" aria-hidden="true">
      <path d="M2 0 H38 L20 30 Z" fill="currentColor"/>
      <rect x="18" y="20" width="4" height="504" fill="currentColor"/>
      <path d="M2 544 H38 L20 514 Z" fill="currentColor"/>
    </svg>

    <div class="truck-art" role="img" aria-label="Outline illustration of a bucket truck with its boom raised"></div>

    <section class="contact">
      <p class="contact-lead">FOR SERVICE CALL</p>
      <p class="contact-phone">800-555-0147</p>
      <p class="contact-email">Service@PanelCareLighting.com</p>
    </section>
  </main>
</body>
</html>
```